Decorative concrete business needs new business cards

Our company attracts homeowners and business with disposable cash. We are a artistic decorative coatings company that will transform your driveway, patio, floors or counter tops into a work of art. We also engrave logos and designs right into the concrete! We are upscale and very professional company. I am open for rearranging our logo on the business card and also to different color patterns. We like the blue and black as in BrushNest's logo. We also like blue and orange/yellow.

Target Market(s)

Adults 30-70

Industry/Entity Type

Concrete

Contact Information for Business Card

Simple: Name, phone, email, website and social media icons

Font styles to use
Serif

Colors

Designer to choose colors to be used in the design.

Requirements
Must have
• Must present a professional upscale appearance. I have attached before and after photos that show you what our industry does. Maybe I will have before and after photo on back of card.
Nice to have
• Artistic, but bold. Nothing whimsical or cute.
Should not have
• Should not have cartoon or childlike appearance.

```html
<!DOCTYPE html>
<html lang="en">
<head>
<meta charset="utf-8">
<title>Stonecraft Finishes – Business Card</title>
<link href="https://fonts.googleapis.com/css2?family=Tinos:wght@400;700&display=swap" rel="stylesheet">
<style>
  :root {
    --stage: #2a2a2c;
    --card-black: #1e1e1f;
    --card-blue: #6570c4;
    --card-blue-deep: #4d58a8;
    --accent-orange: #f26a1b;
    --accent-gold: #f0a020;
    --text-light: #ffffff;
    --text-soft: #e6e6e6;
  }
  * { box-sizing: border-box; margin: 0; padding: 0; }
  html, body {
    width: 1200px; height: 852px; overflow: hidden;
    background: var(--stage);
    font-family: "Tinos", "Times New Roman", serif;
  }
  .canvas { position: relative; width: 1200px; height: 852px; }

  .card {
    position: absolute; left: 280px; width: 640px; height: 366px;
    overflow: hidden; box-shadow: 0 10px 30px rgba(0,0,0,.5);
  }
  /* ---------- front ---------- */
  .card-front {
    top: 48px;
    background: linear-gradient(135deg, #7a84d6 0%, var(--card-blue) 50%, var(--card-blue-deep) 100%);
  }
  .photo {
    position: absolute; top: 20px; height: 200px;
    border: 3px solid #e9ebf7;
  }
  .photo-before { left: 24px; width: 288px;
    background: linear-gradient(160deg, #5b6b4a 0%, #cfd3d6 35%, #eceeef 60%, #9ea3a4 100%); }
  .photo-after { left: 328px; width: 288px;
    background: linear-gradient(150deg, #6d7f55 0%, #a98565 30%, #8b6a4c 60%, #3c3a3b 100%); }
  .photo-label {
    position: absolute; top: 226px; height: 20px; width: 288px;
    background: var(--accent-orange); color: var(--text-light);
    font-size: 14px; font-weight: 700; text-align: center; line-height: 20px;
  }
  .label-before { left: 24px; }
  .label-after { left: 328px; }
  .tagline {
    position: absolute; left: 330px; top: 256px; width: 286px;
    color: var(--text-light); font-size: 12.5px; line-height: 1.3; text-align: right;
  }
  .front-band {
    position: absolute; left: 0; bottom: 0; width: 100%; height: 14px;
    background: var(--accent-orange);
  }
  .brand {
    position: absolute; display: flex; align-items: center; gap: 12px;
    color: var(--text-light); font-weight: 400; letter-spacing: 2px;
  }
  .brand-mark { background: var(--text-light); flex: none; }
  .brand-front { left: 26px; bottom: 36px; font-size: 24px; }
  .brand-front .brand-mark { width: 42px; height: 42px; }

  /* ---------- back ---------- */
  .card-back { top: 438px; background: var(--card-black); }
  .brand-back { left: 60px; top: 120px; font-size: 30px; line-height: 1.05; }
  .brand-back .brand-mark { width: 60px; height: 60px; }
  .brand-back .brand-name { border-left: 1px solid #bbb; padding-left: 12px; }
  .person { position: absolute; right: 40px; top: 34px; text-align: right; }
  .person-name { color: var(--text-light); font-size: 20px; }
  .person-title { color: var(--accent-gold); font-size: 15px; }
  .contacts {
    position: absolute; right: 34px; top: 150px; list-style: none;
    color: var(--text-soft); font-size: 14px; text-align: right;
  }
  .contacts li { display: flex; justify-content: flex-end; align-items: center; gap: 10px; height: 21px; }
  .contacts svg { width: 14px; height: 14px; fill: none; stroke: var(--accent-gold); stroke-width: 1.6; }
  .address {
    position: absolute; left: 60px; top: 262px;
    color: var(--text-soft); font-size: 15px; line-height: 1.35;
  }
  .social { position: absolute; left: 60px; top: 318px; display: flex; gap: 12px; }
  .social span { width: 16px; height: 16px; border-radius: 50%; background: var(--text-light); }
</style>
</head>
<body>
<main class="canvas">

  <section class="card card-front">
    <div class="photo photo-before" role="img" aria-label="Photo of a plain grey concrete driveway before coating"></div>
    <div class="photo photo-after" role="img" aria-label="Photo of the same driveway after a brown stamped decorative coating"></div>
    <div class="photo-label label-before">Before</div>
    <div class="photo-label label-after">After</div>
    <p class="tagline">Will transform your driveway, patio, floors or counter tops into a work of art. We also engrave logos and designs right into the concrete!</p>
    <div class="brand brand-front">
      <span class="brand-mark"></span>
      <span class="brand-name">STONECRAFT FINISHES</span>
    </div>
    <div class="front-band"></div>
  </section>

  <section class="card card-back">
    <div class="brand brand-back">
      <span class="brand-mark"></span>
      <span class="brand-name">STONECRAFT<br>FINISHES</span>
    </div>
    <div class="person">
      <p class="person-name">Martin Hale</p>
      <p class="person-title">Managing Director</p>
    </div>
    <ul class="contacts">
      <li>0400-555-019
        <svg viewBox="0 0 14 14"><rect x="3.5" y="1" width="7" height="12" rx="1.2"/></svg></li>
      <li>0755-501-227
        <svg viewBox="0 0 14 14"><path d="M3 1.5l2.5 2.8-1.3 1.7a8 8 0 0 0 3.8 3.8l1.7-1.3 2.8 2.5-1.8 1.8C6 12.5 1.5 8 1.2 3.3z"/></svg></li>
      <li>martin@stonecraftfinishes.com
        <svg viewBox="0 0 14 14"><rect x="1" y="3" width="12" height="8.5"/><path d="M1 3l6 5 6-5"/></svg></li>
      <li>stonecraftfinishes.com
        <svg viewBox="0 0 14 14"><circle cx="7" cy="7" r="5.8"/><path d="M1.2 7h11.6M7 1.2c-3 3.5-3 8.1 0 11.6M7 1.2c3 3.5 3 8.1 0 11.6"/></svg></li>
    </ul>
    <p class="address">820 Quarry Lane Unit 12<br>Riverton, Il 60099</p>
    <div class="social" aria-label="Social media links">
      <span></span><span></span><span></span><span></span>
    </div>
  </section>

</main>
</body>
</html>
```